We need a single web page design for a promotion. This page will acts as a landing page for users. Please provide us with a cutting edge design. I have attached a previous design used a couple of years ago.

Link: http://www.brightkettlestudio.example/freegift/

The Start Here box needs to look like this:

-Start Here (heading) 
-A box for email addresses to be entered
-Then a check box with "Yes, I have read and agree to the Privacy Policy and agree to receive email marketing from Bright Kettle Studio and acknowledge that I will receive special email offers from our marketing partners, including the Harbor Ledger newsletter."
-A submit button 

All of this information needs to be in one box please.  And please feel free to contact me if you have any questions about this. 

Target Market(s)

Middle aged women (housewives)

Requirements
Must have
• Images must reflect the "500 Photo Prints". The only fields that are necessary are a box for email and a submit button.
Should not have
• The word FREE anywhere on the page

```html
<!DOCTYPE html>
<html lang="en">
<head>
<meta charset="utf-8">
<title>Get 500 Photo Prints Delivered To You</title>
<link href="https://fonts.googleapis.com/css2?family=Alegreya:wght@400;500&family=Arimo:wght@400;700&family=Open+Sans:wght@400;600&display=swap" rel="stylesheet">
<style>
  :root {
    --page-bg: #ece4da;
    --frame: #ffffff;
    --wave: #e6e4e2;
    --panel-top: #f3ede4;
    --panel-bottom: #e2d4bf;
    --orange: #f7830f;
    --orange-light: #fba341;
    --ink: #222222;
    --fine-ink: #3a3a3a;
    --link: #1060d0;
  }
  * { box-sizing: border-box; margin: 0; padding: 0; }
  html, body { width: 1200px; height: 900px; overflow: hidden; }
  body { background: var(--page-bg); font-family: "Arimo", Arial, sans-serif; position: relative; }

  .promo-card {
    position: absolute; left: 109px; top: 85px; width: 979px; height: 567px;
    background: var(--frame); border-radius: 9px;
    box-shadow: 0 0 14px rgba(0,0,0,0.12);
  }
  .promo-stage {
    position: absolute; left: 10px; top: 10px; width: 959px; height: 546px;
    border-radius: 8px; overflow: hidden;
  }
  .hero-photo {
    position: absolute; left: 0; top: 60px; width: 959px; height: 434px;
    background:
      radial-gradient(ellipse at 72% 55%, #c7a98a 0%, rgba(199,169,138,0) 40%),
      radial-gradient(ellipse at 55% 30%, #9aa28a 0%, rgba(154,162,138,0) 45%),
      linear-gradient(180deg, #5d6650 0%, #7a6e58 45%, #8b6a48 75%, #6a4a30 100%);
  }
  .header-wave { position: absolute; left: 0; top: 0; width: 959px; height: 160px; }
  .headline {
    position: absolute; left: 0; top: 4px; width: 959px; text-align: center;
    font-family: "Alegreya", Georgia, serif; font-weight: 400; font-size: 55px;
    color: #fff; letter-spacing: 0; line-height: 60px; padding-left: 8px;
  }
  .headline-note {
    position: absolute; right: 30px; top: 58px;
    font-family: "Alegreya", Georgia, serif; font-size: 11px; color: #fff;
  }

  .signup-panel { position: absolute; left: 46px; top: 113px; width: 336px; height: 381px; }
  .signup-panel svg { position: absolute; inset: 0; }
  .start-badge { position: absolute; left: 27px; top: 61px; width: 292px; height: 60px; }
  .start-badge span {
    position: absolute; left: 0; top: 0; width: 292px; height: 48px; line-height: 49px;
    text-align: center; font-family: "Open Sans", sans-serif; font-size: 37px; color: #fff;
    letter-spacing: -0.5px; padding-right: 8px;
  }
  .email-field {
    position: absolute; left: 32px; top: 133px; width: 269px; height: 36px;
    border: 1px solid #c8c0b4; background: #fff;
    font-family: "Arimo", Arial, sans-serif; font-size: 14px; color: #777;
    padding: 0 9px; line-height: 34px;
  }
  .consent { position: absolute; left: 20px; top: 182px; width: 290px; }
  .consent-box {
    position: absolute; left: 0; top: 5px; width: 10px; height: 10px;
    background: #fff; border: 1px solid #bfb6a8;
  }
  .consent p {
    margin-left: 13px; font-size: 12px; line-height: 22.3px; color: var(--ink);
  }
  .consent u { text-decoration: underline; }
  .studio-name {
    position: absolute; left: 38px; top: 300px; display: flex; align-items: center; gap: 6px;
    font-family: "Arimo", Arial, sans-serif; font-size: 13px; color: #1468c4;
  }
  .studio-name i { display: block; width: 12px; height: 12px; background: #555; }
  .submit-button {
    position: absolute; left: 96px; top: 325px; width: 120px; height: 44px;
    border-radius: 22px; border: 3px solid #f7e9d6;
    background: linear-gradient(180deg, var(--orange-light) 0%, var(--orange) 55%, #e8720a 100%);
    font-family: "Open Sans", sans-serif; font-size: 20px; color: #fff; text-align: center;
    line-height: 38px; box-shadow: 0 1px 3px rgba(0,0,0,0.2);
  }

  .benefit-band {
    position: absolute; left: 0; top: 494px; width: 959px; height: 52px;
    background: linear-gradient(180deg, #1a63cf 0%, #1e6ad6 100%);
    font-family: "Alegreya", Georgia, serif; font-size: 24px; color: #fff;
  }
  .benefit-band span { position: absolute; top: 10px; }

  .fine-print {
    position: absolute; left: 142px; top: 674px; width: 920px; text-align: center;
    font-size: 10.4px; line-height: 18px; color: var(--fine-ink);
  }
  .fine-print .offer-note { font-weight: 700; font-size: 10.6px; margin-bottom: 18px; color: #222; }
  .fine-print p + p { margin-top: 18px; }
  .fine-print a { color: var(--link); }
  .page-links {
    position: absolute; left: 0; top: 873px; width: 1200px; text-align: center;
    font-size: 10.6px; color: #333;
  }
  .page-links a { color: var(--link); text-decoration: none; margin: 0 10px; }
</style>
</head>
<body>
  <div class="promo-card">
    <div class="promo-stage">
      <div class="hero-photo" role="img" aria-label="Photo of a smiling father pushing a toddler in a stroller along an autumn woodland path while a mother photographs them"></div>

      <svg class="header-wave" viewBox="0 0 959 160" aria-hidden="true">
        <defs>
          <linearGradient id="headerBlue" x1="0" y1="0" x2="1" y2="1">
            <stop offset="0" stop-color="#0a4aaa"/>
            <stop offset="0.55" stop-color="#1565c8"/>
            <stop offset="1" stop-color="#3fb2ea"/>
          </linearGradient>
        </defs>
        <path d="M0 0 H959 V158 C860 95 700 62 560 62 C380 62 180 95 0 115 Z" fill="var(--wave)"/>
        <path d="M0 0 H959 V146 C860 84 700 52 560 52 C380 52 180 85 0 105 Z" fill="url(#headerBlue)"/>
      </svg>
      <h1 class="headline">Get 500 Photo Prints Delivered To You</h1>
      <div class="headline-note">With Offer Redemption</div>

      <div class="signup-panel">
        <svg viewBox="0 0 336 381" aria-hidden="true">
          <defs>
            <linearGradient id="panelFill" x1="0" y1="0" x2="0" y2="1">
              <stop offset="0" stop-color="var(--panel-top)"/>
              <stop offset="0.25" stop-color="#e6dbcc"/>
              <stop offset="1" stop-color="var(--panel-bottom)"/>
            </linearGradient>
          </defs>
          <path d="M0 381 V60 C0 22 30 2 75 2 C170 2 270 25 336 50 V381 Z" fill="url(#panelFill)"/>
          <path d="M3 381 V62 C3 26 32 6 75 6 C165 6 262 27 333 53" fill="none" stroke="#fbf8f3" stroke-width="3"/>
        </svg>
        <div class="start-badge">
          <svg width="292" height="60" viewBox="0 0 292 60" aria-hidden="true">
            <rect x="0" y="0" width="292" height="48" rx="24" fill="var(--orange)"/>
            <path d="M240 47 L256 61 L266 47 Z" fill="var(--orange)"/>
          </svg>
          <span>START HERE</span>
        </div>
        <div class="email-field">Enter Your Email Address</div>
        <div class="consent">
          <span class="consent-box"></span>
          <p>YES, I have read and agree to the <u>Privacy Policy</u> and agree to receive email marketing from Bright Kettle Studio and acknowledge that I will receive special email offers from our marketing partners, including the Harbor Ledger newsletter.</p>
        </div>
        <div class="studio-name"><i></i>BrightKettleStudio.example</div>
        <div class="submit-button">SUBMIT</div>
      </div>

      <div class="benefit-band">
        <span style="left:32px">Professional Quality Photos</span>
        <span style="left:353px">Unlimited Storage</span>
        <span style="left:582px">Share With Your Family &amp; Friends</span>
      </div>
    </div>
  </div>

  <div class="fine-print">
    <div class="offer-note">*OFFER REDEMPTION WILL REQUIRE PARTICIPATION AND / OR PURCHASE OF THIRD PARTY OFFERS.</div>
    <p>To receive the membership incentive gift of Five Hundred (500) photo prints you must complete all of the steps outlined herein. Prospective members must: (a) submit their zip code to determine geographic eligibility; (b) register with a valid and deliverable email address; (c) submit accurate contact and demographic information including a mailing address; <b>(d) Accumulate a total of Twenty Five (25) points by either answering survey questions, completing lead questionnaires, or taking advantage of 3rd party offers.</b> Purchase may be required. Please read participation requirements for details.</p>
    <p>On each page, you will be able to see your current point total and the total number of points necessary to redeem the incentive gift. Upon completion of all <a href="#">requirements</a> and upload of the necessary photos, we will ship the incentive gift to you at no shipping cost. Unless otherwise indicated, participation eligibility is restricted to US residents, 18 and over. Void where prohibited.</p>
  </div>
  <div class="page-links"><a href="#">Privacy Policy</a>|<a href="#">Unsubscribe</a></div>
</body>
</html>
```